Stationary design for IT Consultancy
Stationary Design (Business Cards - Letter Heads - Envelopes - Presentation Folders - Power Point)
Stationary design for IT Consultancy - Information Technology
Creative Brief
Use standard fonts
Optional fonts can be used
Professional
Dean Marlow
Technical Director
14 Brindle Works Oakfield Lane Stoneham Wexshire WX7 2QP
dean.marlow@pivotal-nsg.net
www.pivotal-nsg.net

```html
<!DOCTYPE html>
<html lang="en">
<head>
<meta charset="utf-8">
<title>Pivotal Network Solutions Group – Business Card</title>
<link href="https://fonts.googleapis.com/css2?family=Exo+2:wght@400;600;800&family=Cousine:wght@400;700&display=swap" rel="stylesheet">
<style>
  :root {
    --page-bg: #e9eaee;
    --brand-blue: #2f54c8;
    --brand-blue-dark: #1f3ea6;
    --brand-blue-light: #4a6fe0;
    --card-white: #ffffff;
    --ink-grey: #3a3f4a;
    --shadow: rgba(20, 30, 60, 0.22);
  }
  * { box-sizing: border-box; margin: 0; padding: 0; }
  html, body { width: 1200px; height: 698px; overflow: hidden; }
  body {
    background: var(--page-bg);
    font-family: "Exo 2", Arial, sans-serif;
    position: relative;
  }
  .card {
    position: absolute;
    top: 181px;
    width: 520px;
    height: 336px;
    border-radius: 4px;
    box-shadow: 0 10px 28px var(--shadow);
    overflow: hidden;
  }
  .card--front {
    left: 50px;
    background: linear-gradient(135deg, var(--brand-blue-light) 0%, var(--brand-blue) 50%, var(--brand-blue-dark) 100%);
  }
  .card--back {
    left: 630px;
    background: var(--card-white);
  }
  .front-decor {
    position: absolute;
    left: -60px;
    bottom: -120px;
    width: 360px;
    height: 360px;
    border-radius: 50%;
    background: rgba(255, 255, 255, 0.08);
  }
  .wordmark {
    display: flex;
    align-items: center;
    gap: 10px;
  }
  .wordmark__dot {
    width: 22px;
    height: 22px;
    border-radius: 50%;
    flex: none;
  }
  .wordmark__name {
    font-weight: 800;
    letter-spacing: 2px;
    line-height: 1;
  }
  .wordmark__tagline {
    font-weight: 600;
    letter-spacing: 3.2px;
    font-size: 10px;
    margin-top: 4px;
  }
  .card--front .wordmark {
    position: absolute;
    right: 42px;
    top: 40px;
    color: var(--card-white);
  }
  .card--front .wordmark__dot { background: var(--card-white); }
  .card--front .wordmark__name { font-size: 34px; }

  .card--back .wordmark {
    position: absolute;
    left: 34px;
    top: 132px;
    color: var(--brand-blue);
  }
  .card--back .wordmark__dot { background: var(--brand-blue); width: 26px; height: 26px; }
  .card--back .wordmark__name { font-size: 40px; }

  .person {
    position: absolute;
    right: 30px;
    top: 30px;
    text-align: right;
    color: var(--brand-blue);
  }
  .person__name { font-weight: 800; font-size: 19px; }
  .person__role { font-weight: 600; font-size: 14px; margin-top: 1px; }

  .contact {
    position: absolute;
    right: 30px;
    top: 92px;
    text-align: right;
    font-family: "Cousine", "Courier New", monospace;
    font-size: 10.5px;
    line-height: 1.55;
    color: var(--ink-grey);
  }
  .address {
    position: absolute;
    left: 30px;
    bottom: 44px;
    font-family: "Cousine", "Courier New", monospace;
    font-size: 10.5px;
    color: var(--ink-grey);
  }
  .web-band {
    position: absolute;
    left: 0;
    right: 0;
    bottom: 0;
    height: 30px;
  }
  .web-band__url {
    position: absolute;
    right: 30px;
    bottom: 8px;
    font-family: "Cousine", "Courier New", monospace;
    font-weight: 700;
    font-size: 11px;
    color: var(--card-white);
  }
</style>
</head>
<body>
  <section class="card card--front" aria-label="Business card front">
    <div class="front-decor"></div>
    <div class="wordmark">
      <span class="wordmark__dot"></span>
      <div>
        <div class="wordmark__name">PIVOTAL</div>
        <div class="wordmark__tagline">NETWORK SOLUTIONS GROUP</div>
      </div>
    </div>
  </section>

  <section class="card card--back" aria-label="Business card back">
    <div class="person">
      <div class="person__name">Dean Marlow</div>
      <div class="person__role">Technical Director</div>
    </div>
    <div class="contact">
      <div>+44 (0)7700 900 418</div>
      <div>dean.marlow@pivotal-nsg.net</div>
      <div>Skype: marlowdean</div>
    </div>

    <div class="wordmark">
      <span class="wordmark__dot"></span>
      <div>
        <div class="wordmark__name">PIVOTAL</div>
        <div class="wordmark__tagline">NETWORK SOLUTIONS GROUP</div>
      </div>
    </div>

    <div class="address">14 Brindle Works Oakfield Lane Stoneham Wexshire WX7 2QP</div>

    <svg class="web-band" viewBox="0 0 520 30" preserveAspectRatio="none" aria-hidden="true">
      <path d="M0 30 L0 22 Q260 6 520 0 L520 30 Z" fill="var(--brand-blue)"/>
    </svg>
    <div class="web-band__url">www.pivotal-nsg.net</div>
  </section>
</body>
</html>
```